Brisk Talent Circle boutique mgt consulting group 5 page web design

I need a 4 - 5 page website that professionally presents the business and what we do/ offer to potential clients. We are a boutique based consultancy business that is cutting edge, focuses on revenue and profit acceleration for our customers primarily focused on (but looking to expand outside of ) the consumer goods and property/ building markets. We are passionate about seeing our clients grow their business and our Experts are not traditional consultants, rather are senior executive experts that specialise in sales, marketing, leadership, coaching, supply chain functions at C suite and below.

I have just had a new logo created and so would like to replicate this feel through the website please.

The final Website design needs to communicate a new era of consulting and freelance experts where technology will support our offer.. it needs to be be on trend, animated, modern, professional and primarily researched by clients on their mobile devices. Whilst a consultancy I don't want our clients to feel it looks the same as a traditional consultancy...

Videos will be added later.

For basic content feel please see existing www.brisktalentcircle.example website.
I would expect a landing page, our services, about us/ who we are, clients we work with.

The type of website I like the feel of is:
http://cartlumen.example.au

Target Market(s)

Business to Business Manufacturers/ Retailers/ Property

Industry/Entity Type

Management Consulting

Coding

Coded - Design and coding required

Number of Pages Required

5+ page

Font styles to use
Sans Serif

Colors

Designer to choose colors to be used in the design.

Requirements
Must have
• 5 pages including landing page, our services, about us/ who we are, clients we work with.
• Modern, professional look
• demonstrate the services
• ability to add video and content later
• Use the logo
• ability to scroll and look up on mobile devices
Nice to have
• Use my logo as watermark
• Moving images
• I like this website:
• https://venwixa.example
• http://cartlumen.example.au
• other websites :
• https://talorbin.example
Should not have
• The look of a traditional Big 4 consulting firm
• Be fixed and static website

```html
<!DOCTYPE html>
<html lang="en">
<head>
<meta charset="utf-8">
<title>Our Services – Brisk Talent Circle</title>
<link href="https://fonts.googleapis.com/css2?family=Roboto:wght@300;400;500;700;900&display=swap" rel="stylesheet">
<style>
:root{
  --navy:#0d3b72;
  --blue:#1769c2;
  --blue-bright:#2a7fd8;
  --topbar:#0a2f5c;
  --ink:#1d2a3a;
  --text:#3c4652;
  --muted:#6c7784;
  --light:#eef1f4;
  --white:#ffffff;
  --dark:#1c232b;
  --footer:#f4f5f6;
}
*{box-sizing:border-box;margin:0;padding:0}
html,body{width:1200px;height:4100px;overflow:hidden}
body{font-family:"Roboto",Arial,sans-serif;color:var(--text);background:var(--white);position:relative}
.wrap{width:1040px;margin:0 auto;position:relative}

/* top bar */
.topbar{height:40px;background:var(--topbar);color:var(--white);font-size:14px}
.topbar .wrap{display:flex;align-items:center;justify-content:space-between;height:40px}
.topbar-contact{display:flex;gap:18px;align-items:center}
.topbar-mail{display:flex;align-items:center;gap:6px;color:#cfe0f3}
.phone-badge{background:var(--blue-bright);padding:6px 12px;border-radius:3px;display:flex;align-items:center;gap:6px;font-weight:500}

/* header */
.site-header{height:140px;background:var(--white);border-bottom:1px solid #e3e7eb}
.site-header .wrap{display:flex;align-items:center;justify-content:space-between;height:140px}
.brand{display:flex;align-items:center;gap:12px}
.brand-mark{width:34px;height:34px;background:var(--blue)}
.brand-name{font-size:26px;font-weight:700;color:var(--blue)}
.main-nav{display:flex;gap:10px}
.main-nav a{font-size:15px;font-weight:500;color:var(--ink);text-decoration:none;padding:12px 20px;border-radius:3px}
.main-nav a.active{background:var(--blue);color:var(--white)}

/* hero */
.hero{height:320px;position:relative;overflow:hidden}
.hero-photo{position:absolute;inset:0;background:linear-gradient(120deg,#0b3a78 0%,#1a5fae 45%,#3b86d4 75%,#1c5aa2 100%)}
.hero-title{position:absolute;left:80px;top:130px;display:flex;align-items:center;gap:16px;color:var(--white);font-size:46px;font-weight:700;letter-spacing:1px}

/* intro */
.intro{height:100px;display:flex;align-items:center;justify-content:center;background:var(--white)}
.intro h2{font-size:25px;font-weight:700;color:var(--navy)}

/* service bands */
.band{position:relative;overflow:hidden}
.band-photo{position:absolute;inset:0}
.band .wrap{position:relative;z-index:1}
.band h3{font-size:32px;font-weight:700;margin-bottom:28px}
.band p{font-size:15.5px;line-height:1.65;margin-bottom:18px}
.band h4{font-size:16px;font-weight:500;margin-bottom:6px}

.sales{height:420px;background:var(--light)}
.sales .band-photo{background:linear-gradient(90deg,rgba(238,241,244,1) 35%,rgba(205,214,224,.9) 70%,#b7c3d0 100%)}
.sales .wrap{padding-top:70px}
.sales h3{color:var(--navy)}
.sales p{color:var(--ink);width:1000px}

.consumer{height:680px;background:var(--dark)}
.consumer .band-photo{background:linear-gradient(160deg,#2c3540 0%,#151b22 40%,#3a3a3a 70%,#20262d 100%)}
.consumer .wrap{padding-top:100px}
.consumer h3{color:var(--white);text-align:right}
.consumer p{color:#e8ecf0}

.shopper{height:540px;background:#f3f4f6}
.shopper .band-photo{background:linear-gradient(90deg,#d4d8dd 0%,#e9ebee 30%,#f4f5f7 60%,#f7f8f9 100%)}
.shopper .wrap{padding-top:80px}
.shopper h3{color:var(--navy)}
.shopper p{color:var(--ink);margin-bottom:14px}
.shopper h4{color:var(--ink)}

.change{height:400px;background:var(--dark)}
.change .band-photo{background:linear-gradient(200deg,#2f3945 0%,#1a2028 50%,#303841 100%)}
.change .wrap{padding-top:90px;text-align:right}
.change h3{color:var(--white)}
.change p{color:#e8ecf0}

.supply{height:360px;background:#eef0f3}
.supply .band-photo{background:linear-gradient(180deg,#e7eaee 0%,#f3f4f6 45%,#dfe3e8 100%)}
.supply .wrap{padding-top:80px}
.supply h3{color:var(--navy)}
.supply p{color:var(--ink)}

/* contact form */
.contact-form{height:480px;background:var(--blue)}
.contact-form .wrap{padding-top:60px;width:920px}
.contact-form h2{color:var(--white);text-align:center;font-size:32px;font-weight:500;margin-bottom:60px}
.field-row{display:flex;gap:26px;margin-bottom:22px}
.field{flex:1;height:42px;border:1px solid rgba(255,255,255,.75);color:var(--white);font-size:14px;padding:12px 14px}
.field.comment{height:110px;flex:none;width:100%}
.submit{display:block;width:180px;margin:28px auto 0;height:44px;border:1px solid var(--white);background:var(--white);color:var(--blue);font-size:14px;font-weight:500;text-align:center;line-height:44px}

/* contact info */
.contact-info{height:540px;background:var(--white)}
.contact-info .wrap{display:flex;gap:60px;padding-top:70px}
.map{width:500px;height:400px;background:linear-gradient(135deg,#dfe6dc 0%,#e9ede6 40%,#cfdbe6 70%,#dde5ec 100%)}
.contact-details h2{font-size:34px;font-weight:700;color:var(--blue);margin-bottom:18px}
.contact-details .lead{font-size:15px;line-height:1.6;color:var(--muted);width:440px;margin-bottom:40px}
.detail{display:flex;align-items:center;gap:18px;margin-bottom:26px;font-size:15px;color:var(--ink);line-height:1.5}
.detail-icon{width:46px;height:46px;border-radius:50%;border:1px solid #cfd6de;display:flex;align-items:center;justify-content:center;flex:none}
.divider{width:440px;height:1px;background:#dfe3e8;margin-bottom:26px}

.site-footer{height:80px;background:var(--footer);border-top:1px solid #e3e7eb}
.site-footer .wrap{display:flex;align-items:center;justify-content:center;height:80px;font-size:14px;color:var(--muted)}
.site-footer .page-no{position:absolute;right:0}
</style>
</head>
<body>

<div class="topbar">
  <div class="wrap">
    <span>Welcome To Brisk Talent Circle</span>
    <div class="topbar-contact">
      <span class="topbar-mail">
        <svg width="14" height="11" viewBox="0 0 14 11"><rect x="0.5" y="0.5" width="13" height="10" fill="none" stroke="#cfe0f3"/><path d="M1 1l6 5 6-5" fill="none" stroke="#cfe0f3"/></svg>
        clientsupport@brisktalentcircle.example
      </span>
      <span class="phone-badge">
        <svg width="12" height="12" viewBox="0 0 24 24"><path fill="#fff" d="M6.6 10.8a15 15 0 006.6 6.6l2.2-2.2a1 1 0 011-.25 11.4 11.4 0 003.6.57 1 1 0 011 1V20a1 1 0 01-1 1A17 17 0 013 4a1 1 0 011-1h3.5a1 1 0 011 1c0 1.25.2 2.45.57 3.6a1 1 0 01-.25 1z"/></svg>
        0400 318 572
      </span>
    </div>
  </div>
</div>

<header class="site-header">
  <div class="wrap">
    <div class="brand"><span class="brand-mark"></span><span class="brand-name">Brisk Talent Circle</span></div>
    <nav class="main-nav">
      <a href="#">HOME</a>
      <a href="#">ABOUT</a>
      <a href="#" class="active">SERVICE</a>
      <a href="#">CLIENT</a>
      <a href="#">CONTACT US</a>
    </nav>
  </div>
</header>

<section class="hero">
  <div class="hero-photo" role="img" aria-label="Blue-toned photo of a modern city office skyline"></div>
  <h1 class="hero-title">
    <svg width="40" height="40" viewBox="0 0 24 24"><path fill="#fff" d="M9 4h6a2 2 0 012 2v1h3a2 2 0 012 2v10a2 2 0 01-2 2H4a2 2 0 01-2-2V9a2 2 0 012-2h3V6a2 2 0 012-2zm0 3h6V6H9z"/></svg>
    OUR SERVICES
  </h1>
</section>

<section class="intro">
  <h2>We Are Proven Experts In The Consumer Products, Building And Healthcare Industries</h2>
</section>

<section class="band sales">
  <div class="band-photo" role="img" aria-label="Faded photo of a team meeting around a table"></div>
  <div class="wrap">
    <h3>Sales Growth:</h3>
    <p>"We are passionate about helping to embed global best practice sales and marketing processes including corporate JBP (joined up business planning) processes, Pricing and Trading Terms strategies. We look to work with our clients to provide improved capability training with our own sales capability tool to support progress tracking, and work closely with our channel partners to support benchmark sales and negotiation training. We have found as experts that the key is embedding these behaviours as habit rather than one off training courses and so work with our clients on an outcome focused approach to simply accelerate revenue and profit."</p>
    <p>As businesses look to expand their international footprint, we are seeing a rise in export opportunities and demand in different markets such as China or Vietnam. Our Proven Experts can offer support in developing overseas market strategies to accelerate revenue and profit."</p>
  </div>
</section>

<section class="band consumer">
  <div class="band-photo" role="img" aria-label="Dark photo of a shopper browsing products on a phone in a store"></div>
  <div class="wrap">
    <h3>Consumer &amp; E-Commerce:</h3>
    <p>Demand to manage the rise of e-commerce and on-line retailers such as Marketvale over traditional and social media channels are increasingly tailored to win over your customer to help you convert and accelerate revenue. Our Clients have varying degrees of social media presence across Friendloop, Proflink and Snapgrid. Typically, they lack a real social media strategy to bring it all together. We audit, optimise and present a strategy back to the client including targets to drive engagement, followers, likes etc - not many agencies commit to deliver against targets! We can then either boost content either through or developing it or working with the client on what works best. We can then track monthly against these targets.</p>
    <p>We use social media to connect our clients with new and existing customers online. We can create content for all of your social media channels to keep your brand at the forefront of your customers' minds, by reminding them of who you are, what you do and what you can offer them. We develop social media strategies that are tailored specifically for your business, to attract the right kind of customer to your online community. We connect with them, keep them engaged and provide them with a unique online experience to develop long lasting relationships. We also set targets around building a social media audience, increasing a page's reach and boosting customer engagement.</p>
  </div>
</section>

<section class="band shopper">
  <div class="band-photo" role="img" aria-label="Faded photo of a person wearing a virtual reality headset"></div>
  <div class="wrap">
    <h3>Shopper Marketing &amp; Virtual Reality:</h3>
    <h4>For our Retail &amp; Consumer Good Clients:</h4>
    <p>We have partnered with an immersive facility company to be able to bring to you a full breed shopper research platform that helps more quickly predict and proactively alter real shopper behaviour. This can save significant costs on in-store trials and go-to-market experience and the timing of the past. This groundbreaking software platform also links to a 3D-based reference where we are working with our retail clients to build the store. Immerse ourselves within it, move fixtures and fittings and test new signage and where product will be placed - all in real time. The real power though is the data behind it to provide our Client's improved insights. We use the data to work with our clients to accelerate revenue in a virtual world, making quick commercial decisions even before a product has been launched or a brick has been laid.</p>
    <h4>For our Building Products clients:</h4>
    <p>We are able immerse our clients in buildings or apartments before they have been built to understand key insights. Imagine the ability to showcase or change accessories or provide upgrade packages to their customers that they can actually "touch and feel". All this accelerates revenue and profit with our clients.</p>
    <h4>For our Medical Products clients:</h4>
    <p>We work with our clients to help educate the administering of medical products through training - imagine the ability to train in real time just how you administer for the patient.</p>
  </div>
</section>

<section class="band change">
  <div class="band-photo" role="img" aria-label="Dark photo of a business leader addressing a group"></div>
  <div class="wrap">
    <h3>Change Transformation</h3>
    <p>Our Proven Experts work with C suite and below to embed corporate leadership behaviours and help create high performing teams from a habit across the business to accelerate revenue and profit.<br>
    We can help to facilitate workshops to support outcome focused initiatives where appropriate working alongside our clients on the change transformation journey.</p>
  </div>
</section>

<section class="band supply">
  <div class="band-photo" role="img" aria-label="Light illustration of a supply chain diagram linking market, consumer, distributer and supplier"></div>
  <div class="wrap">
    <h3>Supply Chain:</h3>
    <p>We help develop existing supplier relationships and increase levels of supplier collaboration, via S&amp;OP process improvement, strategic sourcing capability and with a high level of stakeholder engagement.</p>
  </div>
</section>

<section class="contact-form">
  <div class="wrap">
    <h2>Contact Form</h2>
    <div class="field-row">
      <div class="field">First Name*</div>
      <div class="field">Last Name*</div>
      <div class="field">Email*</div>
    </div>
    <div class="field comment">Comment*</div>
    <div class="submit">SUBMIT NOW</div>
  </div>
</section>

<section class="contact-info">
  <div class="wrap">
    <div class="map" role="img" aria-label="Street map of central Sydney showing the office location"></div>
    <div class="contact-details">
      <h2>CONTACT US</h2>
      <p class="lead">Our Clients are all different. Please call us to help us better understand how we can accelerate your business.</p>
      <div class="detail">
        <span class="detail-icon"><svg width="18" height="22" viewBox="0 0 24 30"><path fill="#6c7784" d="M12 0a10 10 0 00-10 10c0 7.5 10 20 10 20s10-12.5 10-20A10 10 0 0012 0zm0 14a4 4 0 110-8 4 4 0 010 8z"/></svg></span>
        <span>Brisk Talent Circle Pty Ltd, Sydney,<br>NSW 2000</span>
      </div>
      <div class="divider"></div>
      <div class="detail">
        <span class="detail-icon"><svg width="20" height="15" viewBox="0 0 20 15"><rect x="1" y="1" width="18" height="13" fill="none" stroke="#6c7784" stroke-width="1.5"/><path d="M1.5 1.5l8.5 7 8.5-7" fill="none" stroke="#6c7784" stroke-width="1.5"/></svg></span>
        <span>Mail: clientsupport@brisktalentcircle.example</span>
      </div>
      <div class="divider"></div>
      <div class="detail">
        <span class="detail-icon"><svg width="18" height="18" viewBox="0 0 24 24"><path fill="#6c7784" d="M6.6 10.8a15 15 0 006.6 6.6l2.2-2.2a1 1 0 011-.25 11.4 11.4 0 003.6.57 1 1 0 011 1V20a1 1 0 01-1 1A17 17 0 013 4a1 1 0 011-1h3.5a1 1 0 011 1c0 1.25.2 2.45.57 3.6a1 1 0 01-.25 1z"/></svg></span>
        <span>Phone: 0400 318 572</span>
      </div>
    </div>
  </div>
</section>

<footer class="site-footer">
  <div class="wrap">
    <span>Copyrights © 2017 Brisk Talent Circle. All Rights Reserved.</span>
    <span class="page-no">C20</span>
  </div>
</footer>

</body>
</html>
```